Health & Beauty Company- Business Card Design

Two-sided business card design and logo design.

Company markets and sells otc treatments for the health and beauty industry. Marketing products to doctors, pharmacists and retail drug companies like tormundos, pqz and lumo fex.

Designs should be submitted as vector based PDFs. To keep your text in vector format, our printer recommends applications like Adobe Illustrator, Adobe InDesign and more recent versions of Adobe Photoshop.

Target Market(s)

Drug stores, doctors and pharmacists

Industry/Entity Type

Printer

Requirements
Must have
• Back side of business card should include company logo and our tagline: "Innovating the Health & Beauty Experience"

Company name acronym must be included: QTRM

```html
<!DOCTYPE html>
<html lang="en">
<head>
<meta charset="utf-8">
<title>QTRM Business Card Design</title>
<link rel="stylesheet" href="https://fonts.googleapis.com/css2?family=Bebas+Neue&family=Questrial&family=PT+Sans&display=swap">
<style>
  :root {
    --board: #231f20;
    --card: #ffffff;
    --brand: #e8843a;
  }
  html, body { margin: 0; padding: 0; overflow: hidden; background: var(--board); }
  .board { position: relative; width: 1200px; height: 900px; background: var(--board); overflow: hidden; }
  .card { position: absolute; background: var(--card); color: var(--brand); }
  .card--rounded { border-radius: 62px; }
  .card > * { position: absolute; margin: 0; line-height: 1; white-space: nowrap; }
  .wordmark { font-family: "Bebas Neue", sans-serif; font-weight: 400; letter-spacing: 1px; }
  .tagline { font-family: "Questrial", sans-serif; font-size: 14.5px; }
  .emblem { border-radius: 50%; background: radial-gradient(circle, #f2a25f 0%, var(--brand) 75%); }
  .contact { font-family: "PT Sans", sans-serif; }
  .contact--name, .contact--company { font-size: 13.5px; }
  .contact--line { font-size: 9.5px; }
</style>
</head>
<body>
<main class="board">

  <!-- Rounded set -->
  <section class="card card--rounded" style="left:62px;top:22px;width:458px;height:271px;">
    <div class="emblem" role="img" aria-label="Company emblem area" style="left:205px;top:28px;width:48px;height:48px;"></div>
    <h2 class="wordmark" style="left:0;width:458px;text-align:center;top:92px;font-size:80px;">QTRM</h2>
    <p class="tagline" style="left:0;width:458px;text-align:center;top:176px;">Innovating the Health &amp; Beauty Experince</p>
  </section>

  <section class="card card--rounded" style="left:60px;top:315px;width:462px;height:270px;">
    <div class="emblem" role="img" aria-label="Company emblem area" style="left:48px;top:68px;width:84px;height:84px;"></div>
    <h2 class="wordmark" style="left:174px;top:76px;font-size:80px;">QTRM</h2>
    <p class="tagline" style="left:0;width:462px;text-align:center;top:168px;">Innovating the Health &amp; Beauty Experince</p>
  </section>

  <section class="card card--rounded" style="left:72px;top:607px;width:456px;height:270px;">
    <p class="contact contact--name" style="left:74px;top:31px;">Name xxxxx</p>
    <p class="contact contact--line" style="left:77px;top:52px;">President &amp; CEO</p>
    <h2 class="wordmark" style="left:66px;top:108px;font-size:34px;">QTRM</h2>
    <div class="emblem" role="img" aria-label="Company emblem area" style="left:50px;top:150px;width:84px;height:84px;"></div>
    <p class="contact contact--company" style="left:261px;top:79px;">Company</p>
    <p class="contact contact--line" style="left:260px;top:100px;">Address xxxxxxxxxxxx</p>
    <p class="contact contact--line" style="left:260px;top:120px;">City, State, Zip</p>
    <p class="contact contact--line" style="left:260px;top:148px;">xxx.xxx.xxxx</p>
    <p class="contact contact--line" style="left:260px;top:167px;">xxx.xxx.xxxx</p>
    <p class="contact contact--line" style="left:260px;top:202px;">xxxxxxxxxxxx@xxxxxxxxx.com</p>
    <p class="contact contact--line" style="left:260px;top:226px;">xxxxxxxx.xxxxxxxx</p>
  </section>

  <!-- Square set -->
  <section class="card" style="left:684px;top:30px;width:464px;height:270px;">
    <div class="emblem" role="img" aria-label="Company emblem area" style="left:212px;top:26px;width:48px;height:48px;"></div>
    <h2 class="wordmark" style="left:0;width:476px;text-align:center;top:90px;font-size:80px;">QTRM</h2>
    <p class="tagline" style="left:0;width:474px;text-align:center;top:173px;">Innovating the Health &amp; Beauty Experince</p>
  </section>

  <section class="card" style="left:686px;top:316px;width:460px;height:269px;">
    <div class="emblem" role="img" aria-label="Company emblem area" style="left:52px;top:64px;width:86px;height:86px;"></div>
    <h2 class="wordmark" style="left:172px;top:73px;font-size:80px;">QTRM</h2>
    <p class="tagline" style="left:0;width:460px;text-align:center;top:166px;">Innovating the Health &amp; Beauty Experince</p>
  </section>

  <section class="card" style="left:684px;top:604px;width:464px;height:275px;">
    <p class="contact contact--name" style="left:82px;top:37px;">Name xxxxx</p>
    <p class="contact contact--line" style="left:86px;top:59px;">President &amp; CEO</p>
    <h2 class="wordmark" style="left:76px;top:118px;font-size:34px;">QTRM</h2>
    <div class="emblem" role="img" aria-label="Company emblem area" style="left:60px;top:156px;width:86px;height:86px;"></div>
    <p class="contact contact--company" style="left:283px;top:86px;">Company</p>
    <p class="contact contact--line" style="left:282px;top:108px;">Address xxxxxxxxxxxx</p>
    <p class="contact contact--line" style="left:282px;top:127px;">City, State, Zip</p>
    <p class="contact contact--line" style="left:282px;top:157px;">xxx.xxx.xxxx</p>
    <p class="contact contact--line" style="left:282px;top:176px;">xxx.xxx.xxxx</p>
    <p class="contact contact--line" style="left:282px;top:212px;">xxxxxxxxxxxx@xxxxxxxxx.com</p>
    <p class="contact contact--line" style="left:282px;top:236px;">xxxxxxxx.xxxxxxxx</p>
  </section>

</main>
</body>
</html>
```